Landing Page Design

We need a landing page template designed to support a clients Zenfy Bidpost Campaigns. The client is called Morlet Plumbing and they install and repair hot water systems (only). They provide no other plumbing services.

We are really looking for a great looking landing page that is both engaging and functional.

Target Market(s)

Residential/Domestic market. Typically wives and partners who are typically home or run the household.

Industry/Entity Type

Plumbing

Number of Pages Required

1 page

Requirements
Must have
• Strong branding
Strong call to actions
Great and obvious looking buttons
Nice to have
• Smart use of colour
Should not have
• The design should not use old-style, serif fonts.

Do not include any plumbing images

```html
<!DOCTYPE html>
<html lang="en">
<head>
<meta charset="utf-8">
<title>Morlet Plumbing – Hot Water Now</title>
<link href="https://fonts.googleapis.com/css2?family=Mulish:wght@400;600;700;800&display=swap" rel="stylesheet">
<style>
:root{
  --page:#e6e6e3;
  --card:#ffffff;
  --cream:#eff1d6;
  --orange:#f38f22;
  --orange-deep:#ec6a34;
  --orange-light:#f5a131;
  --ink:#ef5f3a;
  --white:#ffffff;
}
*{box-sizing:border-box;margin:0;padding:0}
html,body{width:1200px;height:934px;overflow:hidden}
body{background:var(--page);font-family:"Mulish",Arial,sans-serif;position:relative;color:var(--ink)}
.sheet{position:absolute;left:42px;top:0;width:1120px;height:892px;background:var(--card);box-shadow:0 2px 8px rgba(0,0,0,.12)}
.header{position:absolute;left:54px;top:15px;width:1094px;height:117px;background:var(--cream)}
.brand{position:absolute;left:66px;top:52px;display:flex;align-items:center;gap:12px}
.brand-dot{width:28px;height:28px;border-radius:50%;background:var(--orange)}
.brand-name{font-size:34px;font-weight:800;color:var(--orange-deep);letter-spacing:.5px}
.header-call{position:absolute;right:70px;top:94px;font-size:24px;font-weight:700;color:var(--ink)}
.band{position:absolute;top:132px;height:13px;left:54px;width:1094px;display:flex}
.band span:nth-child(1){flex:0 0 426px;background:var(--orange-deep)}
.band span:nth-child(2){flex:0 0 332px;background:var(--orange)}
.band span:nth-child(3){flex:1;background:var(--orange-light)}
.offer{position:absolute;left:54px;top:165px;width:482px;height:518px;background:var(--cream);border-radius:22px 0 0 22px}
.badge{position:absolute;left:36px;top:30px;width:407px;height:60px;background:var(--orange);border-radius:4px;color:var(--white);display:flex;align-items:center;justify-content:center;gap:10px;box-shadow:0 2px 3px rgba(0,0,0,.15)}
.badge strong{font-size:30px;font-weight:800}
.badge small{font-size:19px;font-weight:800}
.offer h2{position:absolute;left:0;right:0;top:140px;text-align:center;font-size:22px;font-weight:800}
.offer-copy{position:absolute;left:33px;top:187px;width:413px;font-size:16.5px;font-weight:700;line-height:22px;text-align:justify}
.offer-copy p{margin-bottom:22px}
.photo{position:absolute;left:534px;top:165px;width:296px;height:710px;background:linear-gradient(110deg,#d9dde0 0%,#bfc4c7 40%,#c9a08c 65%,#7a5a4a 100%)}
.btn{position:absolute;background:var(--orange);color:var(--white);font-weight:800;text-align:center;display:flex;align-items:center;justify-content:center;border-radius:6px;line-height:27px;box-shadow:0 2px 3px rgba(0,0,0,.12)}
.btn-quote{left:58px;top:702px;width:226px;height:75px;font-size:22px}
.btn-site{left:297px;top:702px;width:225px;height:75px;font-size:22px}
.btn-rebates{left:58px;top:800px;width:464px;height:73px;font-size:22px}
.enquiry{position:absolute;left:846px;top:165px;width:300px;height:711px;background:var(--cream);border-radius:16px}
.enquiry-intro{position:absolute;left:20px;top:15px;width:262px;font-size:16px;font-weight:700;line-height:24px;text-align:justify}
.enquiry-intro b{font-size:22px;font-weight:800}
.field-label{position:absolute;left:20px;font-size:13px;font-weight:700;line-height:15px;white-space:nowrap}
.field{position:absolute;left:16px;width:263px;height:42px;background:var(--white);border:4px solid var(--orange);border-radius:8px}
.field-area{height:106px;border-radius:12px}
.submit{position:absolute;left:16px;top:660px;width:263px;height:45px;background:var(--orange);color:var(--white);font-size:17px;font-weight:700;display:flex;align-items:center;justify-content:center;border-radius:4px}
</style>
</head>
<body>
<div class="sheet"></div>
<header class="header">
</header>
<div class="brand"><span class="brand-dot"></span><span class="brand-name">Morlet Plumbing</span></div>
<div class="header-call">Call NOW on 9471 3826</div>
<div class="band"><span></span><span></span><span></span></div>

<section class="offer">
  <div class="badge"><strong>Hot Water Now!</strong><small>SAVE $$$</small></div>
  <h2>Solar Hot Water Systems</h2>
  <div class="offer-copy">
    <p>Engage our routine office cleaning for at least 6 months and receive a FREE Carpet and Window clean! No strings attached, no contracts.</p>
    <p>To take advantage of this great offer call us on 1300 58 71 40 or complete and submit the form on this page.</p>
    <p>At Verolin we provide all your property service needs - painlessly. We understand that cleaning and other property services should be background activities. A set and forget proposition.</p>
  </div>
</section>

<div class="photo" role="img" aria-label="Photo of a woman enjoying a hot shower under running water"></div>

<a class="btn btn-quote">Book a<br>FREE Quote</a>
<a class="btn btn-site">Visit our<br>Website</a>
<a class="btn btn-rebates">Click Here for Information on Rebates</a>

<form class="enquiry">
  <p class="enquiry-intro">Take Advantage of this Great Offer. Contact Us NOW on <b>94713826</b> or Register your Interest Below</p>
  <span class="field-label" style="top:138px">Your First Name:</span><span class="field" style="top:158px"></span>
  <span class="field-label" style="top:211px">Your Surname:</span><span class="field" style="top:231px"></span>
  <span class="field-label" style="top:286px">Your Suburb:</span><span class="field" style="top:306px"></span>
  <span class="field-label" style="top:361px">Best Contact Number:</span><span class="field" style="top:381px"></span>
  <span class="field-label" style="top:436px">Your Email Address:</span><span class="field" style="top:456px"></span>
  <span class="field-label" style="top:511px">Enquiry / Comments:</span><span class="field field-area" style="top:531px"></span>
  <span class="submit">Enquire Now</span>
</form>
</body>
</html>
```